Integrated content management graphic

We are looking for a creative iteration for the attached file. We are currently in the process of renewing our branding and this graphic will be a center piece to our product marketing. Our website is www.brelvonvista.com for more information on products and company.
Future projects are available for designers submitting outstanding concepts and branding capability.
Updates

Project Deadline Extended
Reason: We are in the process of picking our final two.

Target Market(s)

Audience is IT and anyone interested in integrating content management with their ERP/Accounting system.

Industry/Entity Type

Construction

Requirements
Must have
• The design must use the current color scheme associated with our website, yellow, black, grey. White can also be used. The design should be sleek.
Nice to have
• 3D Feel. The wheel could take on a stadium concept in 3d.

```html
<!DOCTYPE html>
<html lang="en">
<head>
<meta charset="utf-8">
<title>Integrated Content Management Wheel – Brelvon Vista</title>
<link rel="stylesheet" href="https://fonts.googleapis.com/css2?family=PT+Sans:wght@700&display=swap">
<style>
  :root{
    --yellow:#f5d40f;
    --black:#111111;
    --dark-grey:#575757;
    --mid-grey:#7a7a7a;
    --light-grey:#b3b3b3;
    --side-black:#1c1c1c;
    --side-dark:#444444;
    --side-light:#9a9a9a;
    --divider:#ffffff;
    --page:#ffffff;
  }
  html,body{margin:0;padding:0;overflow:hidden;background:var(--page);}
  .canvas{width:1200px;height:904px;position:relative;overflow:hidden;background:var(--page);}
  .wheel{display:block;width:1200px;height:904px;}
  .label{font-family:"PT Sans",Arial,sans-serif;font-weight:700;fill:var(--yellow);text-anchor:middle;dominant-baseline:middle;}
  .label--outer{font-size:10.5px;}
  .label--outer-large{font-size:13px;}
  .label--middle{font-size:9px;}
  .label--inner{font-size:7.5px;}
  .label--brand{font-size:17px;}
  .seg{stroke:var(--divider);stroke-width:1.2;}
  .seg--black{fill:var(--black);}
  .seg--dark{fill:var(--dark-grey);}
  .seg--mid{fill:var(--mid-grey);}
  .seg--light{fill:var(--light-grey);}
  .side--black{fill:var(--side-black);}
  .side--dark{fill:var(--side-dark);}
  .side--light{fill:var(--side-light);}
  .hub{fill:var(--black);stroke:var(--light-grey);stroke-width:1.2;}
</style>
</head>
<body>
<div class="canvas">
  <svg class="wheel" viewBox="0 0 600 452" xmlns="http://www.w3.org/2000/svg" role="img" aria-label="Integrated content management wheel">
    <defs>
      <clipPath id="side-clip">
        <path d="M146,160 L146,208 A152 103.4 0 0 0 450,208 L450,160 Z"/>
      </clipPath>
    </defs>

    <!-- disc side wall -->
    <g class="disc-side" clip-path="url(#side-clip)">
      <rect class="side--black" x="140" y="150" width="106" height="170"/>
      <rect class="side--light" x="246" y="150" width="104" height="170"/>
      <rect class="side--dark" x="350" y="150" width="106" height="170"/>
    </g>

    <!-- disc top face -->
    <g class="disc-top" transform="translate(298,160) scale(1,0.68)">
      <!-- outer ring: business areas -->
      <path class="seg seg--dark"  vector-effect="non-scaling-stroke" d="M-26.4,-149.7 A152 152 0 0 1 87.2,-124.5 L60.2,-86 A105 105 0 0 0 -18.2,-103.4 Z"/>
      <path class="seg seg--black" vector-effect="non-scaling-stroke" d="M87.2,-124.5 A152 152 0 0 1 151.4,-13.3 L104.6,-9.2 A105 105 0 0 0 60.2,-86 Z"/>
      <path class="seg seg--dark"  vector-effect="non-scaling-stroke" d="M151.4,-13.3 A152 152 0 0 1 52,142.8 L35.9,98.7 A105 105 0 0 0 104.6,-9.2 Z"/>
      <path class="seg seg--light" vector-effect="non-scaling-stroke" d="M52,142.8 A152 152 0 0 1 -52,142.8 L-35.9,98.7 A105 105 0 0 0 35.9,98.7 Z"/>
      <path class="seg seg--black" vector-effect="non-scaling-stroke" d="M-52,142.8 A152 152 0 0 1 -151.4,13.3 L-104.6,9.2 A105 105 0 0 0 -35.9,98.7 Z"/>
      <path class="seg seg--light" vector-effect="non-scaling-stroke" d="M-151.4,13.3 A152 152 0 0 1 -26.4,-149.7 L-18.2,-103.4 A105 105 0 0 0 -104.6,9.2 Z"/>

      <!-- middle ring: software -->
      <path class="seg seg--light" vector-effect="non-scaling-stroke" d="M103.4,18.2 A105 105 0 0 1 -90.9,52.5 L-53.7,31 A62 62 0 0 0 61.1,10.8 Z"/>
      <path class="seg seg--mid"   vector-effect="non-scaling-stroke" d="M-90.9,52.5 A105 105 0 0 1 -90.9,-52.5 L-53.7,-31 A62 62 0 0 0 -53.7,31 Z"/>
      <path class="seg seg--black" vector-effect="non-scaling-stroke" d="M-90.9,-52.5 A105 105 0 0 1 67.5,-80.4 L39.9,-47.5 A62 62 0 0 0 -53.7,-31 Z"/>
      <path class="seg seg--dark"  vector-effect="non-scaling-stroke" d="M67.5,-80.4 A105 105 0 0 1 103.4,18.2 L61.1,10.8 A62 62 0 0 0 39.9,-47.5 Z"/>

      <!-- inner ring: content functions -->
      <path class="seg seg--light" vector-effect="non-scaling-stroke" d="M-43.8,-43.8 A62 62 0 0 1 43.8,-43.8 L24,-24 A34 34 0 0 0 -24,-24 Z"/>
      <path class="seg seg--black" vector-effect="non-scaling-stroke" d="M43.8,-43.8 A62 62 0 0 1 43.8,43.8 L24,24 A34 34 0 0 0 24,-24 Z"/>
      <path class="seg seg--light" vector-effect="non-scaling-stroke" d="M43.8,43.8 A62 62 0 0 1 -43.8,43.8 L-24,24 A34 34 0 0 0 24,24 Z"/>
      <path class="seg seg--black" vector-effect="non-scaling-stroke" d="M-43.8,43.8 A62 62 0 0 1 -43.8,-43.8 L-24,-24 A34 34 0 0 0 -24,24 Z"/>

      <!-- hub -->
      <circle class="hub" vector-effect="non-scaling-stroke" cx="0" cy="0" r="34"/>
    </g>

    <!-- labels: outer ring -->
    <text class="label label--outer" x="292" y="75">Accounting</text>
    <text class="label label--outer" x="382" y="86" transform="rotate(25 382 86)">Project Mgmt</text>
    <text class="label label--outer" x="196" y="118" transform="rotate(-50 196 118)">Property Mgmt</text>
    <text class="label label--outer-large" x="404" y="214" transform="rotate(-38 404 214)">Equipment Mgmt</text>
    <text class="label label--outer-large" x="300" y="262">HR</text>
    <text class="label label--outer-large" x="210" y="222" transform="rotate(32 210 222)">Facilities Mgmt</text>

    <!-- labels: middle ring -->
    <text class="label label--middle" x="276" y="103" transform="rotate(-10 276 103)">DeskSuite</text>
    <text class="label label--middle" x="358" y="126" transform="rotate(62 358 126)">ERP</text>
    <text class="label label--middle" x="340" y="206" transform="rotate(-24 340 206)">Project Mgmt Software</text>
    <text class="label label--middle" x="218" y="166" transform="rotate(-68 218 166)">TeamPoint</text>

    <!-- labels: inner ring -->
    <text class="label label--inner" x="300" y="123">Capture</text>
    <text class="label label--inner" x="343" y="155" transform="rotate(70 343 155)">
      <tspan x="343" dy="-4">Document</tspan><tspan x="343" dy="8">Management</tspan>
    </text>
    <text class="label label--inner" x="298" y="186">Workflow</text>
    <text class="label label--inner" x="257" y="150" transform="rotate(-70 257 150)">Archiving</text>

    <!-- brand name -->
    <text class="label label--brand" x="298" y="160">BV</text>
  </svg>
</div>
</body>
</html>
```